Business Card Design Project

We are rebranding an existing automotive collision repair business. The business is called dentworks garage. I have attached logo but I'm not tied to that. I want to leave this wide open.

I want this card to say we are professional, competent, cutting edge. We are focused on customers and use a lot of the latest technology to make the customer experience different. We sign customers in on iPads. Paperwork I signed electronically and updates are sent via text, email, logging on a website or as they wish. I want this innovation and image to come through in our cards

Target Market(s)

60%. Women 40% men. Age 35-60

Industry/Entity Type

Automotive

Requirements
Must have
• The card must have name, title, phone,email, cell, web page

```html
<!DOCTYPE html>
<html lang="en">
<head>
<meta charset="utf-8">
<title>Dentworks Garage – Business Card</title>
<link rel="stylesheet" href="https://fonts.googleapis.com/css2?family=Roboto:wght@300;400&display=swap">
<style>
  :root {
    --brand-green: #62b946;
    --faint-tint: rgba(255, 255, 255, 0.16);
    --card-white: #f5f7f6;
    --ink-grey: #5a5a5a;
    --page-bg: #ffffff;
    --icon-white: #ffffff;
  }
  * { margin: 0; padding: 0; box-sizing: border-box; }
  html, body {
    width: 1200px;
    height: 800px;
    overflow: hidden;
    background: var(--page-bg);
    font-family: "Roboto", Arial, sans-serif;
  }
  .card-sheet {
    width: 1200px;
    height: 800px;
    display: flex;
    align-items: center;
    justify-content: center;
    gap: 60px;
  }
  .card {
    width: 520px;
    height: 297px;
    display: block;
    filter: drop-shadow(0 14px 12px rgba(0, 0, 0, 0.22));
  }
  .card-front .face { fill: var(--brand-green); }
  .card-back .face { fill: var(--card-white); }
  .deco-name {
    fill: var(--faint-tint);
    font-weight: 400;
    font-size: 21px;
    letter-spacing: 0.5px;
  }
  .holder-name { fill: #ffffff; font-weight: 300; font-size: 30px; }
  .holder-title { fill: #ffffff; font-weight: 300; font-size: 15px; }
  .brand-name { fill: var(--brand-green); font-weight: 400; font-size: 12.5px; }
  .contact-bar, .icon-tile { fill: var(--brand-green); }
  .icon-glyph { fill: none; stroke: var(--icon-white); stroke-width: 1.2; stroke-linecap: round; stroke-linejoin: round; }
  .contact-text { fill: var(--ink-grey); font-weight: 300; font-size: 13.5px; }
</style>
</head>
<body>
<main class="card-sheet">

  <!-- Card front: name and title -->
  <svg class="card card-front" viewBox="0 0 438 250" role="img" aria-label="Card front for Martin Hale, Director">
    <rect class="face" width="438" height="250"/>
    <text class="deco-name" x="424" y="136" text-anchor="end">DENTWORKS GARAGE</text>
    <text class="holder-name" x="48" y="180">Martin Hale</text>
    <text class="holder-title" x="158" y="207">Director</text>
  </svg>

  <!-- Card back: brand and contact details -->
  <svg class="card card-back" viewBox="0 0 438 250" role="img" aria-label="Card back with Dentworks Garage contact details">
    <rect class="face" width="438" height="250"/>

    <text class="brand-name" x="414" y="74" text-anchor="end">DENTWORKS GARAGE</text>

    <g class="contact-list">
      <!-- email -->
      <rect class="contact-bar" x="0" y="123" width="96" height="16"/>
      <rect class="icon-tile" x="104" y="121" width="20" height="20"/>
      <g class="icon-glyph">
        <rect x="108" y="126" width="12" height="9"/>
        <path d="M108 126 L114 131 L120 126"/>
      </g>
      <text class="contact-text" x="135" y="136">hello@dentworksgarage.com</text>

      <!-- web -->
      <rect class="contact-bar" x="0" y="146" width="96" height="16"/>
      <rect class="icon-tile" x="104" y="144" width="20" height="20"/>
      <g class="icon-glyph">
        <circle cx="114" cy="154" r="6"/>
        <ellipse cx="114" cy="154" rx="2.6" ry="6"/>
        <path d="M108 154 H120"/>
      </g>
      <text class="contact-text" x="135" y="159">www.dentworksgarage.com</text>

      <!-- phone -->
      <rect class="contact-bar" x="0" y="169" width="96" height="16"/>
      <rect class="icon-tile" x="104" y="167" width="20" height="20"/>
      <g class="icon-glyph">
        <path d="M109 171 L111.5 171 L113 174.5 L111.5 175.8 C112.5 178 114 179.5 116.2 180.5 L117.5 179 L121 180.5 L121 183 C115 183.5 108.5 177 109 171 Z"/>
      </g>
      <text class="contact-text" x="135" y="182">+1 (800) 555-0142</text>

      <!-- mobile -->
      <rect class="contact-bar" x="0" y="192" width="96" height="16"/>
      <rect class="icon-tile" x="104" y="190" width="20" height="20"/>
      <g class="icon-glyph">
        <rect x="110" y="193" width="8" height="14" rx="1"/>
        <path d="M113 204.5 H115"/>
      </g>
      <text class="contact-text" x="135" y="205">+1 (800) 555-0142</text>
    </g>
  </svg>

</main>
</body>
</html>
```